Design a premium label for the most expensive honey in the world: Manuka honey.

Manuka honey is originaire from New Zealand and recognized for its natural antibacterial activity. Rare and expensive, it is used in hospital as medical grade mainly to cure burns and wounds... Household will use it out of a pot like a "supplement" or to cure all sorts of ailments.
The label must feel:
- Premium and elegant .
- Reflect strongly its origin New Zealand. Use maori design but be careful of copyright. Must be styled.
- Purity and trust it is the real deal. Feel strongly that it is not an ersatz...
- Health and "medical" use.
Label must have:
* Brand: TOROWAI DOWNS
* MANUKA HONEY
* Made in New Zealand
* e250g
* MGO300
Target Market(s)
Export.

```html
<!DOCTYPE html>
<html lang="en">
<head>
<meta charset="utf-8">
<title>Torowai Downs Manuka Honey Label</title>
<link rel="stylesheet" href="https://fonts.googleapis.com/css2?family=Josefin+Sans:wght@300&family=Montserrat:wght@800&family=Tinos&family=Arimo:wght@700&family=Roboto+Condensed:wght@400&display=swap">
<style>
  :root {
    --ink-black: #03040a;
    --ink-deep: #0b0d1c;
    --navy: #1c1f3d;
    --navy-light: #2c3152;
    --slate: #2a2d3b;
    --pink: #f49ad6;
    --white: #ffffff;
    --gold-light: #e8c07a;
    --gold: #c8924a;
    --gold-dark: #8c6430;
    --honey: #f08a0c;
    --honey-deep: #c85a08;
  }
  * { margin: 0; padding: 0; box-sizing: border-box; }
  html, body { width: 1200px; height: 387px; overflow: hidden; background: var(--ink-black); }
  .label { position: relative; width: 1200px; height: 387px; overflow: hidden; }
  .side-panel { position: absolute; top: 0; height: 387px; width: 386px; }
  .side-panel--left { left: 0; background: linear-gradient(90deg, var(--ink-black), var(--ink-deep)); }
  .side-panel--right { left: 814px; background: linear-gradient(120deg, var(--ink-deep) 0%, var(--slate) 100%); }
  .ornament-band {
    position: absolute; left: 0; width: 100%;
    background: linear-gradient(90deg, rgba(200,146,74,0.35), rgba(232,192,122,0.45), rgba(200,146,74,0.35));
  }
  .ornament-band--top { top: 0; height: 56px; -webkit-mask: linear-gradient(180deg, #000 0%, #000 40%, transparent 100%); mask: linear-gradient(180deg, #000 0%, #000 40%, transparent 100%); }
  .ornament-band--bottom { bottom: 0; height: 56px; -webkit-mask: linear-gradient(0deg, #000 0%, #000 40%, transparent 100%); mask: linear-gradient(0deg, #000 0%, #000 40%, transparent 100%); }

  .front-panel {
    position: absolute; left: 386px; top: 0; width: 428px; height: 387px; overflow: hidden;
    background: radial-gradient(ellipse at 85% 10%, var(--navy-light) 0%, var(--navy) 45%, var(--ink-deep) 100%);
    box-shadow: 0 0 18px rgba(0,0,0,0.7);
  }
  .blossom-art {
    position: absolute; left: 0; top: 0; width: 180px; height: 116px;
    background: radial-gradient(ellipse at 45% 40%, rgba(240,170,205,0.85) 0%, rgba(214,90,140,0.55) 45%, rgba(40,60,40,0) 75%);
  }
  .gold-rule { position: absolute; left: 0; top: 0; width: 428px; height: 387px; }
  .brand-name {
    position: absolute; left: 140px; width: 280px; top: 112px; text-align: center;
    font-family: "Josefin Sans", sans-serif; font-weight: 300; font-size: 27px; letter-spacing: 0.5px;
    color: var(--white); white-space: nowrap;
  }
  .product-name {
    position: absolute; left: 140px; width: 280px; top: 152px; text-align: center;
    font-family: "Montserrat", sans-serif; font-weight: 800; font-size: 52px; line-height: 59px;
    color: var(--pink); letter-spacing: 1px;
  }
  .origin {
    position: absolute; left: 140px; width: 280px; top: 273px; text-align: center;
    font-family: "Tinos", serif; font-size: 11.5px; color: var(--white); letter-spacing: 0.3px;
  }
  .weight {
    position: absolute; left: 19px; top: 298px;
    font-family: "Roboto Condensed", sans-serif; font-size: 32px; color: var(--white);
  }
  .grade {
    position: absolute; left: 140px; width: 280px; top: 297px; text-align: center;
    font-family: "Arimo", sans-serif; font-weight: 700; font-size: 38px; letter-spacing: 1px;
    background: linear-gradient(180deg, var(--gold-light), var(--gold) 55%, var(--gold-dark));
    -webkit-background-clip: text; background-clip: text; color: transparent;
  }
  .honeycomb-art {
    position: absolute; left: 0; bottom: 0; width: 428px; height: 42px;
    background: linear-gradient(180deg, rgba(240,138,12,0) 0%, var(--honey) 40%, var(--honey-deep) 100%);
  }
</style>
</head>
<body>
<div class="label">
  <div class="side-panel side-panel--left">
    <div class="ornament-band ornament-band--top" role="img" aria-label="Gold ornamental scallop border"></div>
    <div class="ornament-band ornament-band--bottom" role="img" aria-label="Gold ornamental scallop border"></div>
  </div>

  <div class="front-panel">
    <div class="blossom-art" role="img" aria-label="Pink manuka blossoms on a branch"></div>
    <svg class="gold-rule" viewBox="0 0 428 387" aria-hidden="true">
      <defs>
        <linearGradient id="goldBand" x1="0" y1="1" x2="1" y2="0">
          <stop offset="0" stop-color="#8c6430"/>
          <stop offset="0.5" stop-color="#e8c07a"/>
          <stop offset="1" stop-color="#c8924a"/>
        </linearGradient>
      </defs>
      <polygon points="0,232 235,0 249,0 0,246" fill="url(#goldBand)"/>
      <polygon points="0,250 253,0 268,0 0,265" fill="#3a4068" opacity="0.35"/>
    </svg>
    <div class="brand-name">TOROWAI DOWNS</div>
    <h1 class="product-name">MANUKA<br>HONEY</h1>
    <p class="origin">PRODUCT OF NEW ZEALAND</p>
    <p class="weight">250g</p>
    <p class="grade">MGO300</p>
    <div class="honeycomb-art" role="img" aria-label="Orange honeycomb cells along the bottom edge"></div>
  </div>

  <div class="side-panel side-panel--right">
    <div class="ornament-band ornament-band--top" role="img" aria-label="Gold ornamental scallop border"></div>
    <div class="ornament-band ornament-band--bottom" role="img" aria-label="Gold ornamental scallop border"></div>
  </div>
</div>
</body>
</html>
```